Journeys With Marlowe Business Cards

I need a business card design for my upscale Travel Agency.
Attached you can find my logo.
I would like to include the following:
- Name
- Title
- Phone Number
- Email
- Website
- and then something like: Follow us: JourneysWithMarlowe (and then social media icons in color).
The logo should be in the front and then also the back.
I am also attaching a design that I liked (mostly for the layout) but open to any suggestions
Industry/Entity Type
Travel Agent
Contact Information for Business Card
Name: Celine Drummond
Title: Travel Designer / Owner
Phone: 415-296-0487
Email: celine@journeyswithmarlowe.example
Website: www.JourneysWithMarlowe.example
Social Media Handles for FB,IG, Twitter: JourneysWithMarlowe
Font styles to use
Colors
Designer to choose colors to be used in the design.
Look and feel

```html
<!DOCTYPE html>
<html lang="en">
<head>
<meta charset="utf-8">
<title>Journeys With Marlowe — Business Card</title>
<link rel="stylesheet" href="https://fonts.googleapis.com/css2?family=Barlow:wght@400;500;700&family=Kalam:wght@700&display=swap">
<style>
  :root {
    --canvas: #e9e6e1;
    --card-front: #f2f2f2;
    --card-back: #f4a859;
    --accent: #eba257;
    --ink: #333333;
    --ink-script: #4a4a4a;
    --white: #ffffff;
    --social-one: #6a2c91;
    --social-two: #2aa3dd;
    --social-three: #1d64b0;
  }
  * { box-sizing: border-box; margin: 0; padding: 0; }
  html, body { width: 900px; height: 1200px; overflow: hidden; }
  body {
    position: relative;
    background: var(--canvas);
    font-family: "Barlow", Arial, sans-serif;
    color: var(--ink);
  }
  .card {
    position: absolute;
    left: 75px;
    width: 768px;
    height: 438px;
    border-radius: 18px;
  }
  .card--front { top: 133px; background: var(--card-front); }
  .card--back { top: 629px; height: 439px; background: var(--card-back); }

  .monogram {
    position: absolute;
    left: 40px; top: 36px;
    width: 220px; height: 136px;
    display: flex; align-items: center; justify-content: center;
    font-weight: 500;
    font-size: 96px;
    letter-spacing: 2px;
    color: var(--accent);
  }
  .brand-band {
    position: absolute;
    left: 282px; top: 39px;
    width: 449px; height: 135px;
    background: var(--accent);
    display: flex; align-items: center; justify-content: center;
  }
  .brand-band__name {
    font-weight: 500;
    font-size: 38px;
    color: var(--white);
    white-space: nowrap;
  }

  .holder { position: absolute; left: 46px; top: 214px; }
  .holder__name {
    font-weight: 700;
    font-size: 31px;
    letter-spacing: 2.5px;
    color: var(--accent);
    text-transform: uppercase;
    line-height: 1.1;
  }
  .holder__title { font-size: 21px; line-height: 1.3; margin-top: 2px; }

  .contact-list { position: absolute; left: 46px; top: 314px; list-style: none; }
  .contact-list__item {
    display: flex; align-items: center;
    height: 30.5px;
    font-size: 20px;
  }
  .contact-list__icon { width: 24px; height: 20px; margin-right: 12px; fill: var(--accent); }

  .follow { position: absolute; right: 44px; top: 302px; text-align: center; }
  .follow__label {
    font-family: "Kalam", "Comic Sans MS", cursive;
    font-weight: 700;
    font-size: 25px;
    color: var(--ink-script);
    line-height: 1;
  }
  .follow__channels { display: flex; gap: 9px; margin-top: 14px; justify-content: center; }
  .follow__dot { width: 44px; height: 44px; border-radius: 50%; }
  .follow__dot--one { background: var(--social-one); }
  .follow__dot--two { background: var(--social-two); }
  .follow__dot--three { background: var(--social-three); }

  .back-mark {
    position: absolute; inset: 0;
    display: flex; align-items: center; justify-content: center;
    font-weight: 500;
    font-size: 190px;
    letter-spacing: 6px;
    color: var(--white);
  }
</style>
</head>
<body>

<section class="card card--front" aria-label="Business card front">
  <div class="monogram">JWM</div>
  <div class="brand-band"><span class="brand-band__name">Journeys With Marlowe</span></div>

  <div class="holder">
    <h1 class="holder__name">Celine Drummond</h1>
    <p class="holder__title">Travel Designer / Owner</p>
  </div>

  <ul class="contact-list">
    <li class="contact-list__item">
      <svg class="contact-list__icon" viewBox="0 0 24 20" aria-hidden="true">
        <path d="M2 7c0-3 4-5 10-5s10 2 10 5v2h-5V7c-1-1-3-1.5-5-1.5S8 6 7 7v2H2z"/>
        <path d="M6 10h12l2 8H4z"/>
      </svg>415-296-0487
    </li>
    <li class="contact-list__item">
      <svg class="contact-list__icon" viewBox="0 0 24 20" aria-hidden="true">
        <path d="M2 4h20v1l-10 6L2 5z"/>
        <path d="M2 7l10 6 10-6v10H2z"/>
      </svg>celine@journeyswithmarlowe.example
    </li>
    <li class="contact-list__item">
      <svg class="contact-list__icon" viewBox="0 0 24 20" aria-hidden="true">
        <circle cx="12" cy="10" r="9" fill="none" stroke="var(--accent)" stroke-width="1.8"/>
        <ellipse cx="12" cy="10" rx="4" ry="9" fill="none" stroke="var(--accent)" stroke-width="1.6"/>
        <path d="M3 10h18M5 5h14M5 15h14" stroke="var(--accent)" stroke-width="1.4"/>
      </svg>www.JourneysWithMarlowe.example
    </li>
  </ul>

  <div class="follow">
    <p class="follow__label">Follow us on</p>
    <div class="follow__channels">
      <span class="follow__dot follow__dot--one"></span>
      <span class="follow__dot follow__dot--two"></span>
      <span class="follow__dot follow__dot--three"></span>
    </div>
  </div>
</section>

<section class="card card--back" role="img" aria-label="Card back: orange field with a fine dot pattern behind the large white monogram">
  <div class="back-mark">JWM</div>
</section>

</body>
</html>
```